Fernbrook Dwellings Business Card Design Project

Please create a custom Business Card Design for Fernbrook Dwellings. The logo is attached to this brief.Please include space for
Name Surname
Title (Solutions Specialist)
Phone
Email
Website
Industry/Entity Type
Business
Contact Information for Business Card
Reverse should be printed horizontally and have the following components:
Small version of the logo. (lowest priority)
The words "Real Estate Solutions Company"
A bulleted list (Note: Line breaks are suggestions only):
* BUY, RENOVATE, SELL and RENT:
RESIDENTIAL PROPERTIES
* MAKE CASH OFFERS ON HOUSES IN
ANY CONDITION and IN ANY SITUATION
* SELL PROPERTIES TO INVESTORS
* SOLVE COMPLEX REAL ESTATE
PROBLEMS and TITLE ISSUES
* PRIVATE MONEY INVESTMENT SERVICES
* PAY CASH REWARDS FOR REFERRALS
Included somewhere on the reverse should also be the following:
Office: (425) 555-0183
www.FernbrookDwellings.example
space for civic trade registry logo
Look and feel
Each slider illustrates characteristics of the customer's brand and the style your logo design should communicate.

```html
<!DOCTYPE html>
<html lang="en">
<head>
<meta charset="utf-8">
<title>Fernbrook Dwellings – Business Card</title>
<link href="https://fonts.googleapis.com/css2?family=Exo+2:wght@400;600;700&display=swap" rel="stylesheet">
<style>
  :root {
    --bg: #e9e6e1;
    --card: #ffffff;
    --card-shade: #e4e6e8;
    --blue: #1a78c2;
    --blue-deep: #0f5fa6;
    --blue-light: #5aa9e0;
    --sun: #f3d36a;
    --sun-pale: #fbf1c8;
    --ink: #2b2f33;
    --on-blue: #ffffff;
  }
  * { box-sizing: border-box; margin: 0; padding: 0; }
  html, body { width: 1200px; height: 828px; overflow: hidden; }
  body {
    background: var(--bg);
    font-family: "Exo 2", sans-serif;
    color: var(--ink);
    position: relative;
  }
  .card {
    position: absolute;
    top: 259px;
    width: 540px;
    height: 310px;
    background: linear-gradient(160deg, var(--card) 40%, var(--card-shade) 100%);
    box-shadow: 0 6px 18px rgba(0,0,0,.18);
    overflow: hidden;
  }
  .card--front { left: 40px; }
  .card--back { left: 620px; }
  .card svg.waves { position: absolute; inset: 0; width: 100%; height: 100%; }

  .brand {
    position: absolute;
    display: flex;
    align-items: center;
    gap: 10px;
    color: var(--blue);
    font-weight: 700;
    text-transform: uppercase;
    letter-spacing: .04em;
    white-space: nowrap;
  }
  .brand__dot { border-radius: 50%; background: var(--sun); flex: none; }
  .card--front .brand { left: 70px; top: 128px; font-size: 32px; }
  .card--front .brand__dot { width: 44px; height: 44px; }
  .card--back .brand { right: 20px; top: 240px; font-size: 19px; }
  .card--back .brand__dot { width: 28px; height: 28px; }

  .holder {
    position: absolute;
    right: 28px;
    top: 28px;
    text-align: right;
    text-transform: uppercase;
  }
  .holder__name { color: var(--blue); font-size: 17px; font-weight: 600; letter-spacing: .06em; }
  .holder__title { font-size: 13px; font-weight: 600; letter-spacing: .08em; }

  .address {
    position: absolute;
    right: 28px;
    top: 92px;
    text-align: right;
    font-size: 12px;
    line-height: 1.4;
  }
  .contacts {
    position: absolute;
    right: 28px;
    top: 140px;
    list-style: none;
    font-size: 10.5px;
    line-height: 1.75;
    text-align: right;
  }
  .contacts li { display: flex; justify-content: flex-end; align-items: center; gap: 6px; }
  .contacts svg { width: 10px; height: 10px; fill: var(--blue); flex: none; }

  .services {
    position: absolute;
    left: 16px;
    top: 18px;
    width: 178px;
    color: var(--on-blue);
  }
  .services__tagline {
    font-size: 12.5px;
    font-weight: 700;
    letter-spacing: .02em;
    line-height: 1.2;
    margin-bottom: 8px;
  }
  .services__list {
    list-style: none;
    font-size: 7.6px;
    font-weight: 600;
    line-height: 1.35;
    text-transform: uppercase;
  }
  .services__list li {
    position: relative;
    padding-left: 9px;
    margin-bottom: 3px;
  }
  .services__list li::before {
    content: "";
    position: absolute;
    left: 0;
    top: 3px;
    width: 4px;
    height: 4px;
    border-radius: 50%;
    background: var(--sun);
  }
  .services__office {
    margin-top: 8px;
    font-size: 9.5px;
    line-height: 1.45;
  }
  .registry-badge {
    position: absolute;
    left: 16px;
    bottom: 16px;
    width: 30px;
    height: 30px;
    border-radius: 4px;
    background: var(--on-blue);
    opacity: .9;
  }
</style>
</head>
<body>

<section class="card card--front" aria-label="Card front">
  <svg class="waves" viewBox="0 0 540 310" preserveAspectRatio="none" aria-hidden="true">
    <defs>
      <linearGradient id="frontSwoosh" x1="0" y1="0" x2="1" y2="0">
        <stop offset="0" stop-color="#ffffff" stop-opacity="0"/>
        <stop offset=".5" stop-color="#b9d8ef"/>
        <stop offset="1" stop-color="#7fb8e3"/>
      </linearGradient>
    </defs>
    <path d="M250 0 C330 40 420 40 540 40 L540 0 Z" fill="url(#frontSwoosh)"/>
    <path d="M250 0 C330 30 430 28 540 52" fill="none" stroke="var(--blue)" stroke-width="3"/>
    <path d="M300 0 C380 22 450 20 540 30" fill="none" stroke="var(--blue-light)" stroke-width="1.5"/>
  </svg>
  <div class="brand"><span class="brand__dot"></span>Fernbrook Dwellings</div>
</section>

<section class="card card--back" aria-label="Card back">
  <svg class="waves" viewBox="0 0 540 310" preserveAspectRatio="none" aria-hidden="true">
    <defs>
      <linearGradient id="backBlue" x1="0" y1="0" x2="1" y2="1">
        <stop offset="0" stop-color="var(--blue-light)"/>
        <stop offset="1" stop-color="var(--blue-deep)"/>
      </linearGradient>
      <linearGradient id="sunGlow" x1="0" y1="0" x2="1" y2="0">
        <stop offset="0" stop-color="var(--sun-pale)"/>
        <stop offset="1" stop-color="#ffffff" stop-opacity="0"/>
      </linearGradient>
    </defs>
    <path d="M0 0 L200 0 C290 90 150 200 240 310 L0 310 Z" fill="url(#backBlue)"/>
    <path d="M200 0 C290 90 150 200 240 310 L270 310 C190 200 320 90 215 0 Z" fill="url(#sunGlow)"/>
    <path d="M210 0 C300 95 165 205 252 310" fill="none" stroke="var(--sun)" stroke-width="4"/>
    <path d="M200 0 C290 90 150 200 240 310" fill="none" stroke="var(--blue)" stroke-width="3"/>
  </svg>

  <div class="services">
    <p class="services__tagline">Real Estate Solutions Company</p>
    <ul class="services__list">
      <li>Buy, renovate, sell and rent: residential properties</li>
      <li>Make cash offers on houses in any condition and in any situation</li>
      <li>Sell properties to investors</li>
      <li>Solve complex real estate problems and title issues</li>
      <li>Private money investment services</li>
      <li>Pay cash rewards for referrals</li>
    </ul>
    <p class="services__office">Office: (425) 555-0183<br>www.FernbrookDwellings.example</p>
  </div>
  <div class="registry-badge" role="img" aria-label="civic trade registry badge"></div>

  <div class="holder">
    <p class="holder__name">Mara Ellison</p>
    <p class="holder__title">Solutions Specialist</p>
  </div>

  <p class="address">27 Harbor Court<br>Linden Row WA</p>

  <ul class="contacts">
    <li>(425) 555-0183
      <svg viewBox="0 0 10 10"><path d="M2 0 L4 2 L3 3.5 C4 5 5 6 6.5 7 L8 6 L10 8 L8 10 C4 9 1 6 0 2 Z"/></svg></li>
    <li>(425) 555-0147
      <svg viewBox="0 0 10 10"><path d="M2.5 0 H7.5 V10 H2.5 Z M3.5 1 V8 H6.5 V1 Z"/></svg></li>
    <li>(425) 555-0162
      <svg viewBox="0 0 10 10"><path d="M1 3 H9 V9 H1 Z M3 0 H7 V3 H3 Z"/></svg></li>
    <li>mara@fernbrook.example
      <svg viewBox="0 0 10 10"><path d="M0 2 H10 V8 H0 Z M1 3 L5 6 L9 3 Z" fill-rule="evenodd"/></svg></li>
    <li>www.FernbrookDwellings.example
      <svg viewBox="0 0 10 10"><circle cx="5" cy="5" r="4.5" fill="none" stroke="var(--blue)" stroke-width="1.2"/><path d="M0.5 5 H9.5 M5 0.5 V9.5" stroke="var(--blue)" stroke-width="0.8"/></svg></li>
  </ul>

  <div class="brand"><span class="brand__dot"></span>Fernbrook Dwellings</div>
</section>

</body>
</html>
```